Online video and marketing company business cards

Need to get some new business cards designed to fit with our new logo. The cards should be professional, clean and simple.

Cards should have:

Name
Position
2 line address
telephone
mobile
email address
web address

We need to have our logo and if possible say what we do...
ONLINE FILM PRODUCTION & STRATEGY

Industry/Entity Type

Marketing

```html
<!DOCTYPE html>
<html lang="en">
<head>
<meta charset="utf-8">
<title>Fieldframe business cards</title>
<link rel="stylesheet" href="https://fonts.googleapis.com/css2?family=Roboto+Condensed:wght@300;400;500&display=swap">
<style>
  :root {
    --backdrop: #e4ebf2;
    --card: #ffffff;
    --card-edge: #d9dee5;
    --ink: #3d5a86;
    --brand: #2a5c86;
    --tagline: #a9bfd3;
    --decor: #e2e5ee;
  }
  html, body {
    margin: 0;
    padding: 0;
    width: 1200px;
    height: 900px;
    overflow: hidden;
    background: var(--backdrop);
    font-family: "Roboto Condensed", "Arial Narrow", sans-serif;
  }
  .canvas {
    position: relative;
    width: 1200px;
    height: 900px;
  }
  .card {
    position: absolute;
    left: 320px;
    width: 559px;
    height: 361px;
    background: var(--card);
    border: 1px solid var(--card-edge);
    box-sizing: border-box;
    overflow: hidden;
  }
  .card-front { top: 55px; }
  .card-back { top: 469px; }

  .brand-lockup {
    position: absolute;
    left: 0;
    right: 0;
    top: 148px;
    display: flex;
    align-items: center;
    justify-content: center;
    gap: 10px;
  }
  .brand-dot {
    width: 34px;
    height: 34px;
    border-radius: 50%;
    background: var(--brand);
  }
  .brand-name {
    font-size: 42px;
    font-weight: 500;
    color: var(--brand);
    letter-spacing: -0.5px;
    line-height: 1;
  }

  .decor-circle {
    position: absolute;
    left: 0;
    top: 0;
    width: 559px;
    height: 361px;
  }
  .tagline {
    position: absolute;
    left: 30px;
    top: 340px;
    transform: rotate(-90deg);
    transform-origin: left top;
    font-size: 14px;
    font-weight: 300;
    color: var(--tagline);
    white-space: nowrap;
    letter-spacing: 0.2px;
  }
  .contact {
    position: absolute;
    left: 65px;
    top: 112px;
    color: var(--ink);
    font-size: 15px;
    line-height: 21px;
  }
  .contact p { margin: 0; }
  .person-name { font-size: 19px; line-height: 22px; }
  .person-role { font-size: 10px; line-height: 12px; margin-bottom: 28px !important; }
  .phone-label { display: inline-block; width: 24px; }
  .block-gap { margin-top: 21px !important; }
</style>
</head>
<body>
<main class="canvas">
  <section class="card card-front" aria-label="Card front">
    <div class="brand-lockup">
      <span class="brand-dot"></span>
      <span class="brand-name">Fieldframe</span>
    </div>
  </section>

  <section class="card card-back" aria-label="Card back">
    <svg class="decor-circle" viewBox="0 0 559 361" aria-hidden="true">
      <circle cx="440" cy="262" r="122" fill="none" stroke="var(--decor)" stroke-width="30"/>
    </svg>
    <div class="tagline">online film production &amp; strategy</div>
    <div class="contact">
      <p class="person-name">Daniel Hart</p>
      <p class="person-role">Director</p>
      <p><span class="phone-label">t.</span>+44 20 7946 0321</p>
      <p><span class="phone-label">m.</span>+44 7700 900514</p>
      <p class="block-gap">daniel@fieldframe.tv</p>
      <p>www.fieldframe.tv</p>
      <p class="block-gap">14 Marlow Row</p>
      <p>London N7 2QP U.K.</p>
    </div>
  </section>
</main>
</body>
</html>
```